Bluestone Advisory & Mgmt - Professional Business Cards

Hi!

I am a Real Estate Developer and Construction Consultant.

I have a lot of inspiration from previous designs and would be open to using the attached Designs as a starting point. I would like to see these styles incorporated into your designs.

I really need professional business card to go with it that includes my important info.

Look forward to seeing your designs!.

Target Market(s)

My Target market are building owners, lawyers, consultants.

Industry/Entity Type

Real Estate Development

Contact Information for Business Card

My Name: Dorian Pelkey
My Title: Principle
Company Name: Bluestone Advisory & Mgmt, LLC
Address: 348 West 71st Street, 9th FL New York, NY 10010
Mobile: 917.806.3971
Website: bam-hvx.example

Font styles to use
Serif
Sans Serif

Colors

Designer to choose colors to be used in the design.

Requirements
Must have
• Must incorporate the logo attached or have new that looks similar.
• Must use professional font that will be seen and judged by wealthy land owners and developers.
• Must incorporate some of the color green.
Should not have
• Photo's or pictures of people or buildings of any kind.

```html
<!DOCTYPE html>
<html lang="en">
<head>
<meta charset="utf-8">
<title>Bluestone Advisory &amp; Mgmt – Business Cards</title>
<link rel="stylesheet" href="https://fonts.googleapis.com/css2?family=Abel&family=Raleway:wght@400&display=swap">
<style>
  :root {
    --backdrop: #a09e9f;
    --card-light: #e8e4e5;
    --card-dark: #d6d1d2;
    --brand-green: #72ae78;
    --brand-green-deep: #6aa672;
    --ink-white: #ffffff;
  }
  html, body {
    margin: 0;
    padding: 0;
    width: 1200px;
    height: 1200px;
    overflow: hidden;
    background: var(--backdrop);
  }
  .canvas {
    position: relative;
    width: 1200px;
    height: 1200px;
  }
  .card {
    position: absolute;
    left: 250px;
    width: 700px;
    height: 400px;
    background: linear-gradient(100deg, var(--card-light) 0%, var(--card-dark) 100%);
    overflow: hidden;
  }
  .card--front { top: 147px; }
  .card--back  { top: 652px; }

  .web-strip {
    position: absolute;
    left: 0;
    top: 82px;
    width: 36px;
    height: 263px;
    background: var(--brand-green);
  }
  .web-strip__url {
    position: absolute;
    left: 50%;
    top: 50%;
    transform: translate(-50%, -50%) rotate(90deg);
    white-space: nowrap;
    font-family: "Raleway", sans-serif;
    font-size: 13px;
    letter-spacing: 0.5px;
    color: var(--ink-white);
    text-transform: uppercase;
  }

  .brand-name {
    position: absolute;
    left: 372px;
    top: 210px;
    width: 260px;
    margin: 0;
    font-family: "Raleway", sans-serif;
    font-weight: 400;
    color: var(--brand-green);
    line-height: 1.1;
  }
  .brand-name__main {
    display: block;
    font-size: 40px;
  }
  .brand-name__sub {
    display: block;
    font-size: 17.5px;
    margin-top: 4px;
  }

  .contact-panel {
    position: absolute;
    left: 265px;
    top: 83px;
    width: 435px;
    height: 265px;
    background: linear-gradient(100deg, var(--brand-green) 0%, var(--brand-green-deep) 100%);
    font-family: "Abel", sans-serif;
    color: var(--ink-white);
    text-transform: uppercase;
    font-size: 16.5px;
    letter-spacing: 0.2px;
  }
  .contact-panel p {
    position: absolute;
    left: 29px;
    margin: 0;
    white-space: nowrap;
  }
  .contact-panel__company { top: 38px; }
  .contact-panel__name    { top: 97px; }
  .contact-panel__title   { top: 123px; }
  .contact-panel__address { top: 181px; }
  .contact-panel__phone   { top: 207px; }
</style>
</head>
<body>
<main class="canvas">
  <section class="card card--front" aria-label="Card front">
    <div class="web-strip">
      <span class="web-strip__url">bam-hvx.example</span>
    </div>
    <h1 class="brand-name">
      <span class="brand-name__main">Bluestone</span>
      <span class="brand-name__sub">Advisory Management</span>
    </h1>
  </section>

  <section class="card card--back" aria-label="Card back">
    <div class="contact-panel">
      <p class="contact-panel__company">Bluestone Advisory &amp; Mgmt, LLC</p>
      <p class="contact-panel__name">Dorian Pelkey</p>
      <p class="contact-panel__title">Principle</p>
      <p class="contact-panel__address">348 West 71st Street, 9th FL New York, NY 10010</p>
      <p class="contact-panel__phone">917.806.3971</p>
    </div>
  </section>
</main>
</body>
</html>
```